Solvane Holdings Inc. Business Card Design

My business is custom renovations and homes.I would need to have a new business logo created to go along with my company name. The business card should be of a modern style as this is the market I am focused on. I would need my contact information and website posted on the card. I would also like to list a few of the tasks I conduct on the card (such as: Renovations, Additions, Repairs, New Homes, Design, Consultations). On the reverse of the card I currently have just my logo and my motto, "Shaping Fresh Ground". However, I am open to completely changing everything as I am starting a new year and would like to excel further. Any new ideas and suggestions are always welcomed. Thank you.

Target Market(s)

Upscale residential and commercial renovations and builds

Industry/Entity Type

Business

Contact Information for Business Card

I would like the design to be able to be laser cut or burnt onto a wooden business card. I will be creating one option of cards for really loyal customers (wooden) and a second option for the everyday customer (paper).

Font styles to use
Other font styles liked:
• Calibri / anything of mordern taste

Colors
f37122
5c5c5c
474747
ffffff

Requirements
Must have
• I would like the colours of my business to be a sharp orange and grey. I believe this will symbolize a modern style. I am open to other suggestions if this is not suitable for the designers tastes. My contact info as follows:
• Dirk Malsworth
• President
• Solvane Holdings Inc.
• 555-239-7814
• dirk@solvaneholdings.example
• I would like my website (currently under construction) solvaneholdings.example on the card aswell.
Nice to have
• Along with a modern logo representing Solvane, I would like something on the card besides the logo and contact information. Perhaps a small background design. I feel it may be nice to have my services listed on the card (in smaller font on the bottom) Renovations, Additions, Repairs, Design, Consultations.
Should not have
• The business card should not have too many different colors. Should not have rounded corners.

```html
<!DOCTYPE html>
<html lang="en">
<head>
<meta charset="utf-8">
<title>Solvane Holdings Inc. – Business Card</title>
<link rel="stylesheet" href="https://fonts.googleapis.com/css2?family=Montserrat:wght@400;500;600;700&display=swap">
<style>
  :root {
    --orange: #f37122;
    --card-black: #050505;
    --white: #ffffff;
    --grey-line: #5c5c5c;
    --backdrop: #474747;
  }
  * { box-sizing: border-box; margin: 0; padding: 0; }
  html, body {
    width: 1200px; height: 900px; overflow: hidden;
    background: var(--backdrop);
    font-family: "Montserrat", sans-serif;
  }
  .stage { position: relative; width: 1200px; height: 900px; }
  .card {
    position: absolute;
    width: 600px; height: 343px;
    background: var(--card-black);
    border-radius: 0;
    overflow: hidden;
    box-shadow: 0 14px 30px rgba(0,0,0,.45);
    color: var(--white);
  }
  .card--front { left: 100px; top: 80px; }
  .card--back { left: 500px; top: 470px; }

  .brand-name {
    font-weight: 700;
    color: var(--orange);
    letter-spacing: 1px;
    display: flex; align-items: center; gap: 12px;
    white-space: nowrap;
  }
  .brand-name .brand-square {
    width: 22px; height: 22px; background: var(--orange);
  }

  /* front */
  .card--front .brand-name {
    position: absolute; left: 90px; top: 140px; font-size: 46px;
  }
  .services {
    position: absolute; left: 390px; top: 52px;
    list-style: none; font-size: 15px; line-height: 20px;
  }
  .services li { display: flex; align-items: center; gap: 10px; }
  .services li::before {
    content: ""; width: 7px; height: 7px; border-radius: 50%;
    background: var(--orange);
  }
  .tagline {
    position: absolute; left: 0; right: 0; top: 270px;
    text-align: center; font-size: 17px; font-weight: 500;
    letter-spacing: 1px; text-transform: uppercase;
  }

  /* back */
  .band {
    position: absolute; left: 0; right: 0; top: 72px; height: 34px;
    background: var(--orange);
  }
  .company-pill {
    position: absolute; left: 120px; top: 64px;
    padding: 8px 24px; background: var(--white);
    border: 3px solid var(--card-black); border-radius: 10px;
    color: var(--card-black); font-weight: 700; font-size: 19px;
    letter-spacing: .5px; text-transform: uppercase; white-space: nowrap;
  }
  .card--back .brand-name {
    position: absolute; left: 40px; top: 222px; font-size: 38px;
  }
  .divider {
    position: absolute; left: 310px; top: 140px; width: 1px; height: 160px;
    background: var(--grey-line);
  }
  .contact { position: absolute; left: 334px; top: 140px; right: 20px; }
  .contact__name { color: var(--orange); font-size: 27px; font-weight: 700; white-space: nowrap; }
  .contact__role { font-size: 15px; margin-bottom: 16px; }
  .contact__line {
    display: flex; align-items: center; gap: 10px;
    font-size: 13.5px; line-height: 22px; white-space: nowrap;
  }
  .contact__line svg { width: 13px; height: 13px; flex: none; }
  .accent { color: var(--orange); }
</style>
</head>
<body>
<main class="stage">
  <section class="card card--front">
    <div class="brand-name"><span class="brand-square"></span>Solvane</div>
    <ul class="services">
      <li>Renovations</li>
      <li>Additions</li>
      <li>Repairs</li>
      <li>New Homes</li>
      <li>Design</li>
      <li>Consultations</li>
    </ul>
    <p class="tagline">Shaping Fresh Ground</p>
  </section>

  <section class="card card--back">
    <div class="band"></div>
    <div class="company-pill">Solvane Holdings Inc.</div>
    <div class="brand-name"><span class="brand-square"></span>Solvane</div>
    <div class="divider"></div>
    <div class="contact">
      <p class="contact__name">Dirk Malsworth</p>
      <p class="contact__role">President</p>
      <p class="contact__line">
        <svg viewBox="0 0 24 24"><path fill="#f37122" d="M6.6 10.8a15 15 0 0 0 6.6 6.6l2.2-2.2c.3-.3.7-.4 1-.2 1.1.4 2.3.6 3.6.6.6 0 1 .4 1 1V20c0 .6-.4 1-1 1A17 17 0 0 1 3 4c0-.6.4-1 1-1h3.5c.6 0 1 .4 1 1 0 1.3.2 2.5.6 3.6.1.3 0 .7-.2 1z"/></svg>
        555-239-7814
      </p>
      <p class="contact__line">
        <svg viewBox="0 0 24 24"><rect x="2" y="5" width="20" height="14" rx="2" fill="none" stroke="#f37122" stroke-width="2"/><path d="M2 6l10 7 10-7" fill="none" stroke="#f37122" stroke-width="2"/></svg>
        dirk@solvaneholdings.example
      </p>
      <p class="contact__line">
        <svg viewBox="0 0 24 24"><circle cx="12" cy="12" r="9" fill="none" stroke="#f37122" stroke-width="2"/><path d="M3 12h18M12 3c3 3 3 15 0 18M12 3c-3 3-3 15 0 18" fill="none" stroke="#f37122" stroke-width="1.6"/></svg>
        <span>www.<span class="accent">solvaneholdings</span>.example</span>
      </p>
    </div>
  </section>
</main>
</body>
</html>
```